A4 6 page tri-fold brochure for security screen company

Brochure design and layout for a new company based in the UAE called Harborline Panels. We make clear mesh security screen doors and windows that aesthetically blend with the house, like a fly screen, rather than a traditional heavy looking security screen. We want to project an image of safety and security but with warmth and humanity to it, not just something clinical. Copy hasn't been written yet so use dummy text or pull and adjust copy form our website www.harborlinepanels.example.
Target market: home owners, financially comfortable, possibly with young children or pets.
Purpose of brochure: to have potential clients contact us (via phone, whatsapp, email or through our website) to arrange a free measure and quote.
More details provided in attached word doc brief and product images, logos etc, attached also.
Please see attached brief.

Target Market(s)

Home owners, financially comfortable, possibly with young children or pets.

Industry/Entity Type

Home Improvement

Font styles to use
Serif
Sans Serif

Colors
0255a3
3176b5
85acd3
cfdfed
eaf1f7

Requirements
Must have
• Good clear images with detailed close ups (or call outs) of specific details such as the mesh and locks.
• Contact details to include website www.harborlinepanels.example, phone number: +971 50 318 2609, email address: oliver@harborlinepanels.example
Nice to have
• If your are comfortable using and adjusting the appropriate copy from our website please do so.
• Images - I've included a lot of images so please choose the most appropriate to help sell the product. Some of the better images I like are: _DSC2929, French_Windows, HARBORLINE_PANELS-3204, HARBORLINE_PANELS-3231, HARBORLINE_PANELS-3345, HARBORLINE_PANELS-3354, HARBORLINE_PANELS-3401, Girls room windows1, Girls room windows2, IMG_2968. Please don't limit yourself to these images and use the ones you feel best fit.
Should not have
• Please see attached brief.

```html
<!DOCTYPE html>
<html lang="en">
<head>
<meta charset="utf-8">
<title>Harborline Panels – Tri-fold Brochure</title>
<link rel="stylesheet" href="https://fonts.googleapis.com/css2?family=Roboto+Condensed:wght@300;400;700&family=Crimson+Text:wght@400&display=swap">
<style>
  :root{
    --page-bg:#ececec;
    --navy:#0b3f78;
    --navy-deep:#1c2a36;
    --teal:#4b8f7b;
    --teal-dark:#2f4f5c;
    --teal-text:#17664c;
    --ink:#222;
    --white:#fff;
    --gold:#d9a224;
    --sans:"Roboto Condensed", Arial, sans-serif;
    --serif:"Crimson Text", Georgia, serif;
  }
  *{margin:0;padding:0;box-sizing:border-box}
  html,body{width:1200px;height:1200px;overflow:hidden;background:var(--page-bg)}
  .stage{position:absolute;left:0;top:0;width:1470px;height:1470px;transform:scale(.8163);transform-origin:0 0}
  .panel-label{position:absolute;width:200px;margin-left:-100px;text-align:center;font-family:var(--serif);font-size:26px;color:#111}
  .spread{position:absolute;left:314px;width:843px;height:595px;background:var(--white);overflow:hidden;box-shadow:4px 4px 5px rgba(0,0,0,.55)}
  .spread--outside{top:95px}
  .spread--inside{top:810px}
  .shapes{position:absolute;left:0;top:0;width:843px;height:595px}
  .photo{position:absolute}
  .photo--circle{border-radius:50%;border:3px solid #1a1a1a;box-shadow:4px 5px 6px rgba(0,0,0,.55)}
  .copy{position:absolute;font-family:var(--sans);font-weight:300;font-size:9px;line-height:14px;letter-spacing:-.15px;text-align:justify}
  .headline{position:absolute;font-family:var(--sans);font-weight:400;color:var(--ink)}
  .product-title{position:absolute;font-family:var(--sans);font-weight:400;font-size:18px;line-height:20px;color:var(--teal-text)}
  .brand{position:absolute;display:flex;align-items:center;gap:6px;font-family:var(--sans);font-weight:700;font-size:15px;color:var(--navy)}
  .brand__mark{width:14px;height:14px;background:var(--navy)}
  .seal{position:absolute;border-radius:50%;background:radial-gradient(circle at 40% 35%,#f4c94b,var(--gold) 60%,#9b6c12);box-shadow:2px 3px 4px rgba(0,0,0,.4)}
  .warranty{position:absolute;font-family:var(--sans);font-weight:400;font-size:9px;line-height:14px;color:var(--white);text-align:right;white-space:nowrap}
  .contact{position:absolute;font-family:var(--sans);font-weight:700;font-size:10.5px;line-height:14px;letter-spacing:.4px;color:var(--white);text-align:center}
</style>
</head>
<body>
<div class="stage">
  <div class="panel-label" style="left:472px;top:24px">Panel 5</div>
  <div class="panel-label" style="left:749px;top:24px">Panel 6</div>
  <div class="panel-label" style="left:1024px;top:24px">Panel 1</div>

  <!-- Outside spread -->
  <section class="spread spread--outside">
    <svg class="shapes" viewBox="0 0 843 595" aria-hidden="true">
      <defs>
        <linearGradient id="room" x1="0" y1="0" x2="1" y2="1"><stop offset="0" stop-color="#5fb0e0"/><stop offset=".6" stop-color="#bfc9cf"/><stop offset="1" stop-color="#8c7d6d"/></linearGradient>
        <linearGradient id="villa" x1="0" y1="0" x2="0" y2="1"><stop offset="0" stop-color="#9cc3e6"/><stop offset=".25" stop-color="#efe3b4"/><stop offset=".8" stop-color="#dccb96"/><stop offset="1" stop-color="#b7a77a"/></linearGradient>
      </defs>
      <rect x="0" y="0" width="276" height="420" fill="url(#room)"/>
      <rect x="276" y="0" width="567" height="460" fill="url(#villa)"/>
      <polygon points="276,12 420,12 558,70 558,330 276,595" fill="#fff"/>
      <rect x="276" y="0" width="567" height="12" fill="var(--navy-deep)"/>
      <polygon points="0,160 300,345 186,595 0,595" fill="var(--teal)"/>
      <polygon points="120,230 276,330 276,420" fill="#6fb09c" opacity=".7"/>
      <polygon points="186,595 556,300 600,330 250,595" fill="var(--teal-dark)"/>
      <polygon points="250,595 600,330 660,385 843,345 843,595" fill="var(--navy)"/>
      <polygon points="558,440 640,360 700,455" fill="#2f4f5c" opacity=".8"/>
    </svg>
    <div class="photo" role="img" aria-label="Child's bedroom with blue curtains and a sliding screen door" style="left:0;top:0;width:276px;height:150px"></div>

    <p class="copy" style="left:14px;top:250px;width:225px;color:#1d4a3b;text-align:left">The main components of the doors and windows are finished with a high quality electrical charged powder coating to ensure corrosion resistance and exterior good looks. The locks and handles are also subjected to durability testing having to pass a functional 50,000 cycle test. All this is to ensure your screens are the most durable on the market and will last at least 10 years.</p>
    <div class="photo photo--circle" role="img" aria-label="Close-up of stainless steel mesh" style="left:146px;top:382px;width:120px;height:120px;background:radial-gradient(circle,#8a8a8a,#3a3a3a)"></div>
    <div class="photo photo--circle" role="img" aria-label="Close-up of door handle and lock" style="left:24px;top:455px;width:120px;height:120px;background:linear-gradient(90deg,#4a4440 55%,#d98b5a 56%)"></div>

    <p class="headline" style="left:296px;top:43px;width:242px;font-size:17.5px;line-height:18px;text-align:justify;text-align-last:center">Super strong, stainless steel mesh security screens that look stylish and won't break.</p>
    <div class="photo" role="img" aria-label="Villa entrance with sliding screen door and potted palms" style="left:316px;top:115px;width:204px;height:90px;background:linear-gradient(90deg,#7a5a35,#c59a63 40%,#3e3a34 60%,#b88a55)"></div>
    <p class="copy" style="left:296px;top:222px;width:242px;color:var(--ink)">Harborline Panels are manufactured to the highest quality controlled standards by an ISO 9001 certified company. The high tensile, woven, stainless steel mesh has been powdered coated and tested to resist the harsh Middle East elements. With a very small amount of maintenance, your Harborline Panels will resist the elements and maintain their great look for years to come.</p>
    <div class="seal" style="left:322px;top:382px;width:70px;height:70px"></div>
    <p class="warranty" style="left:400px;top:398px;width:138px">Should<br>you have any<br>problems with<br>your Harborline Panels,<br>we offer a 10 year warranty<br>on all stainless steel mesh and<br>aluminium products and 1 year on<br>component parts.</p>
    <p class="contact" style="left:321px;top:540px;width:200px">www.harborlinepanels.example<br>oliver@harborlinepanels.example<br>+971 50 318 2609</p>

    <div class="brand" style="left:640px;top:38px"><span class="brand__mark"></span>Harborline Panels</div>
    <div class="photo photo--circle" role="img" aria-label="Macro view of woven steel mesh" style="left:578px;top:352px;width:100px;height:100px;background:radial-gradient(circle,#4a5058,#15191e)"></div>
    <p class="headline" style="left:566px;top:470px;width:270px;font-size:20px;line-height:30px;color:var(--white);text-align:center">Seriously strong screens that<br>let the breeze in and keep<br>intruders (and bugs) out!</p>
  </section>

  <!-- Inside spread -->
  <section class="spread spread--inside">
    <svg class="shapes" viewBox="0 0 843 595" aria-hidden="true">
      <defs>
        <linearGradient id="strip" x1="0" y1="0" x2="1" y2="0"><stop offset="0" stop-color="#bcd6e4"/><stop offset=".45" stop-color="#e8d9cf"/><stop offset=".7" stop-color="#e6b9c2"/><stop offset="1" stop-color="#8a6a55"/></linearGradient>
      </defs>
      <polygon points="45,0 550,0 284,185" fill="url(#strip)"/>
      <polygon points="30,0 62,0 284,180 530,0 550,12 284,212" fill="var(--teal)"/>
      <polygon points="0,0 60,0 20,70 0,100" fill="var(--navy)"/>
      <polygon points="745,0 843,0 843,32" fill="var(--navy-deep)"/>
      <polygon points="0,525 246,595 0,595" fill="var(--navy-deep)"/>
    </svg>
    <div class="photo photo--circle" role="img" aria-label="Child looking out through a screen door to the garden" style="left:416px;top:40px;width:140px;height:140px;background:linear-gradient(180deg,#e9eef2,#9cb58a)"></div>

    <p class="headline" style="left:14px;top:105px;width:200px;font-size:15px;line-height:19px">Sleep easy, and<br>enjoy the fresh winter<br>breeze,&nbsp; knowing your loved<br>ones are safe and secure.</p>
    <div class="photo" role="img" aria-label="Living room opening to terrace through screen doors" style="left:20px;top:195px;width:225px;height:100px;background:linear-gradient(90deg,#5a3c2a,#d8c4a2 45%,#8a6a48)"></div>
    <p class="copy" style="left:14px;top:305px;width:265px;color:var(--ink)">Our mesh screens may look like ordinary insect screens, but the stainless steel mesh passes tough Knife Shear Testing ensuring total security and peace of mind. Manufactured and constructed using a patented framing system the screens offer the protection of steel, a barrier for bugs and all while offering unobstructed views.</p>
    <div class="photo photo--circle" role="img" aria-label="Pet door fitted in a hinged screen door" style="left:20px;top:384px;width:136px;height:136px;background:linear-gradient(90deg,#c7703d,#7a6a58 50%,#c7703d)"></div>
    <div class="photo photo--circle" role="img" aria-label="Dining room with glass screen doors" style="left:174px;top:442px;width:136px;height:136px;background:linear-gradient(180deg,#e2d2b4,#9aa4a8 60%,#3a3a3a)"></div>

    <h2 class="headline" style="left:312px;top:193px;font-size:17px;line-height:20px">Sliding Screen Doors</h2>
    <p class="copy" style="left:288px;top:218px;width:274px;color:var(--ink)">Harborline Panels sliding screen doors are the number one choice in the UAE for home villa security and insect protection. They provide a robust and durable solution to replace those constantly deteriorating fly screens found on many villas. These screens are a great choice for high traffic areas such as backyards and entertainment areas as the screen will last for years.</p>
    <div class="photo" role="img" aria-label="Bedroom balcony with sliding screen door" style="left:294px;top:310px;width:160px;height:122px;background:linear-gradient(180deg,#eef0ee,#bfc7b8 60%,#c96a86)"></div>
    <div class="photo" role="img" aria-label="Dining area with sliding screen door to garden" style="left:395px;top:460px;width:160px;height:120px;background:linear-gradient(90deg,#cfcbc6,#e9e3da 50%,#8d6a48)"></div>

    <h2 class="product-title" style="left:572px;top:11px">Hinged Screen Doors</h2>
    <p class="copy" style="left:572px;top:35px;width:258px;color:var(--teal-text);text-align:left">Harborline Panels hinged screen doors offer a high level of protection to your home while providing a clear outdoor view. All hinged security doors are fitted with a 3 point locking system for added security. For those with cats and dogs, we also offer the option of fitting a pet door to our range of hinged doors.</p>
    <div class="photo" role="img" aria-label="Hinged screen door on villa entrance" style="left:610px;top:106px;width:76px;height:101px;background:linear-gradient(90deg,#d9b887,#3b3330 45%,#d9b887)"></div>
    <div class="photo" role="img" aria-label="Open hinged screen door" style="left:708px;top:106px;width:76px;height:101px;background:linear-gradient(90deg,#e8c58a,#2f2b28 50%,#efe3c9)"></div>
    <h2 class="product-title" style="left:572px;top:211px">Hinged Screen Doors</h2>
    <p class="copy" style="left:572px;top:234px;width:258px;color:var(--teal-text)">Perfect for inward and outward opening doors, these French doors maintain that classic open space feeling that we all love. They offer a clear view and natural airflow while still maintaining the renowned toughness of stainless steel mesh.</p>
    <div class="photo" role="img" aria-label="Wooden French doors with screen doors" style="left:637px;top:298px;width:128px;height:98px;background:linear-gradient(90deg,#8a4a22,#c58a55 40%,#e9e6e0 60%,#3a3a3a)"></div>
    <h2 class="product-title" style="left:580px;top:402px;text-transform:uppercase">Window Screens</h2>
    <p class="copy" style="left:572px;top:426px;width:258px;line-height:13.5px;color:var(--teal-text)">Harborline Panels custom mesh window screens are designed to protect all shapes and sizes of window openings. Available in sliding, French, fixed and hinged panels they provide a high level of security without compromising your view.</p>
    <div class="photo" role="img" aria-label="Villa windows fitted with mesh screens" style="left:637px;top:484px;width:128px;height:96px;background:linear-gradient(90deg,#e7d8b0,#2c3036 45%,#e7d8b0)"></div>
  </section>

  <div class="panel-label" style="left:472px;top:1418px">Panel 2</div>
  <div class="panel-label" style="left:749px;top:1418px">Panel 3</div>
  <div class="panel-label" style="left:1024px;top:1418px">Panel 4</div>
</div>
</body>
</html>
```